Website Header for new website

We need a header/banner design for our revised website. Here is the link to our existing website lorimakwell.me and to our new website in process agewiseplus.us
Area of expertise is older adults, baby boomers and caregivers
This is an individual, professional website for a Speaker, Keynoter, Author, Brocaster

Target Market(s)

Event planners, broadcasters, publishers

Font styles to use
Serif

```html
<!DOCTYPE html>
<html lang="en">
<head>
<meta charset="utf-8">
<title>Lori Makwell</title>
<link href="https://fonts.googleapis.com/css2?family=Alegreya:wght@400;700&family=Roboto:wght@400;500;700&display=swap" rel="stylesheet">
<style>
:root{
  --navy:#2b3a8f;
  --magenta:#a0156e;
  --plum:#6b2a7a;
  --card:#3b35f5;
  --page:#ececec;
  --ink:#111;
  --white:#fff;
}
*{margin:0;padding:0;box-sizing:border-box}
html,body{width:1200px;height:547px;overflow:hidden;background:var(--page);font-family:"Roboto",sans-serif}
.site{position:relative;width:1200px;height:547px}
.topbar{position:absolute;left:0;top:0;width:1200px;height:61px;background:var(--white);box-shadow:0 2px 6px rgba(0,0,0,.08);z-index:3}
.brand{position:absolute;left:21px;top:11px;width:176px;height:35px;border:2px solid #222;font-family:"Alegreya",serif;font-size:19px;letter-spacing:.5px;color:#222;display:flex;align-items:center;justify-content:center}
.nav a{position:absolute;top:20px;font-size:11px;color:#222;text-decoration:none;white-space:nowrap}
.hero{position:absolute;left:0;top:61px;width:1200px;height:264px;overflow:hidden;background:linear-gradient(90deg,#f4f4f6 0%,#d9d6df 30%,#b9bccb 60%,#9ea3b6 100%)}
.crowd{position:absolute;inset:0}
.portrait{position:absolute;left:100px;top:0;width:230px;height:264px;background:linear-gradient(180deg,#d9a98a 0%,#d9763f 50%,#c9521c 100%);opacity:.85}
.name-box{position:absolute;left:356px;top:41px;width:298px;height:52px;background:linear-gradient(90deg,var(--navy),#4a2f8a 70%,var(--magenta));color:var(--white);font-family:"Alegreya",serif;font-weight:700;font-size:38px;display:flex;align-items:center;justify-content:center;letter-spacing:.5px}
.rule{position:absolute;left:356px;top:109px;width:844px;height:2px;background:linear-gradient(90deg,var(--navy),var(--magenta))}
.roles{position:absolute;top:118px;font-family:"Alegreya",serif;font-size:21.5px;line-height:31.5px;color:var(--plum);white-space:nowrap}
.featured{position:absolute;left:806px;top:15px;background:var(--navy);color:var(--white);font-size:9px;font-weight:700;letter-spacing:1px;padding:3px 6px;border-bottom:2px solid var(--magenta)}
.badges{position:absolute;left:806px;top:39px;display:flex;gap:11px}
.badge{width:53px;height:53px;background:var(--white);border-radius:8px;display:flex;align-items:center;justify-content:center;box-shadow:0 1px 3px rgba(0,0,0,.15)}
.badge span{display:block;width:32px;height:16px;border-radius:3px;background:#c9cbd6}
.card{position:absolute;top:294px;background:var(--card);color:var(--white);text-align:center}
.card h2{font-weight:500;font-size:16px;margin-top:18px}
.thumb{position:absolute}
.podcast-text{position:absolute;left:80px;top:46px;width:180px;font-size:11px;line-height:17.5px;color:#dcdcff;white-space:nowrap;text-align:center}
.podcast-text b{font-weight:400;color:var(--white)}
.card-line{position:absolute;left:16px;right:16px;top:120px;height:1px;background:rgba(255,255,255,.15)}
.social{margin-top:12px;font-size:13px;font-weight:700;letter-spacing:.3px}
.social span{margin:0 5px}
.email{margin-top:22px;font-size:11px;font-weight:500}
.panel{position:absolute;left:184px;top:454px;width:821px;height:93px;background:var(--white)}
.panel-rule{position:absolute;left:362px;top:28px;width:98px;height:2px;background:#2a4fc8}
.panel h3{position:absolute;left:55px;top:62px;font-size:16.5px;font-weight:700;color:var(--ink)}
.panel-photo{position:absolute;left:427px;top:61px;width:339px;height:32px;background:linear-gradient(90deg,#f3ecea,#e9e1de)}
</style>
</head>
<body>
<div class="site">
  <header class="topbar">
    <div class="brand">LORI MAKWELL</div>
    <nav class="nav">
      <a style="left:276px">Home</a>
      <a style="left:337px">Meet Lori</a>
      <a style="left:432px">Speaker/Spokesperson &#8964;</a>
      <a style="left:586px">Blog</a>
      <a style="left:639px">Podcast</a>
      <a style="left:711px">Books</a>
      <a style="left:772px">Work with Lori</a>
      <a style="left:892px">Contact</a>
      <a style="left:962px">Press</a>
    </nav>
  </header>

  <section class="hero">
    <div class="crowd" role="img" aria-label="Blurred audience at a conference"></div>
    <svg width="1200" height="264" style="position:absolute;left:0;top:0">
      <defs>
        <linearGradient id="band" x1="0" y1="0" x2="0" y2="1">
          <stop offset="0" stop-color="#a0156e"/><stop offset="1" stop-color="#3d2a80"/>
        </linearGradient>
      </defs>
      <polygon points="248,0 332,0 124,264 38,264" fill="url(#band)"/>
      <polygon points="1200,118 1200,264 1124,264" fill="#3d2069"/>
    </svg>
    <div class="portrait" role="img" aria-label="Portrait photo of Lori Makwell"></div>
    <div class="name-box">Lori Makwell</div>
    <div class="rule"></div>
    <div class="roles" style="left:356px">Dynamic Keynoter<br>Motivating Speaker<br>Influential Broadcaster</div>
    <div class="roles" style="left:600px">Prolific Author<br>Enterainting Blogger<br>Effective Trainer</div>
    <div class="featured">FEATURED ON</div>
    <div class="badges">
      <div class="badge"><span></span></div>
      <div class="badge"><span></span></div>
      <div class="badge"><span></span></div>
      <div class="badge"><span></span></div>
      <div class="badge"><span></span></div>
      <div class="badge"><span></span></div>
    </div>
  </section>

  <div class="card" style="left:184px;width:267px;height:136px">
    <h2>Our Latest Podcast</h2>
    <div class="thumb" role="img" aria-label="Podcast guest photo" style="left:16px;top:47px;width:59px;height:59px;background:linear-gradient(160deg,#6b4a35,#1e1a18)"></div>
    <p class="podcast-text"><b>Podcast Guest: Nora Delvin, CORA</b><br>AgeWise Plus Radio, July 26–<br>Guest: Nora Delvin, ...<b>Click Here</b></p>
    <div class="card-line"></div>
  </div>

  <div class="card" style="left:461px;width:267px;height:134px">
    <h2>Speaker/Spokesperson</h2>
    <div class="thumb" role="img" aria-label="Speaker at a podium" style="left:16px;top:44px;width:60px;height:74px;background:linear-gradient(180deg,#3a4660,#5a4c44 70%,#b9b3aa)"></div>
    <p style="position:absolute;left:100px;top:46px;width:130px;font-size:11px">Topics &amp; Testimonials</p>
  </div>

  <div class="card" style="left:737px;width:267px;height:131px">
    <h2>Follow Us on Social Media</h2>
    <div class="social"><span>ProLink</span><span>Chirp</span><span>Circle</span></div>
    <div class="email">lorimakwell@inbox.me</div>
  </div>

  <section class="panel">
    <div class="panel-rule"></div>
    <h3>Influence &amp; Entertain</h3>
    <div class="panel-photo" role="img" aria-label="Lori Makwell speaking on stage"></div>
  </section>
</div>
</body>
</html>
```